Binary Options Robot Landing Page

I need a landing page for a campaign advertising binary options robot trading. The campaign and overall look and feel should be inspired by this brand: https://quellmarktrader.com/

The screenshots you want to add from the trading area you can simple google. We will replace any screenshots with actual screenshots from our binary trading software.

You can also copy the text since we will replace the text as well.

The name to advertise is "Vextra Pilot - Bright Paths" and will be featured on www.vextrapilot.ws

What is important is the overall look!
- Vextra Pilot
- Clean Design
- Nice colors
- Makes you want to signup and trade!

Target Market(s)

People who wants to earn some extra money by investing and trading options online.

Industry/Entity Type

Advertising

Logo Text

VExtraPilot - Bright Path

Number of Pages Required

1 page

Colors

Designer to choose colors to be used in the design.

Requirements
Must have
• New Logo or remake of current logo
• Design for web resolution
• Design for mobile resolution
• Signup form as attached but designed more flashy!
• The chat popup may not block crucial elements of the design
Nice to have
• Screenshots that makes people interested to signup
• Catchy phrases that will get people interested in the product
• You are allowed to copy or partly copy the current logo
• Design a contact page
Should not have
• US flags

```html
<!DOCTYPE html>
<html lang="en">
<head>
<meta charset="utf-8">
<title>Vextra Pilot - Bright Paths</title>
<link rel="stylesheet" href="https://fonts.googleapis.com/css2?family=Montserrat:wght@400;500;600;700;800&display=swap">
<style>
:root{
  --teal:#5db4b0;
  --teal-dark:#3f9a96;
  --orange:#efa21a;
  --navy:#1f2b3a;
  --ink:#2f3a46;
  --muted:#6c7a86;
  --pale:#e6f3f3;
  --chat:#8e9bb0;
  --white:#ffffff;
}
*{box-sizing:border-box;margin:0;padding:0}
html,body{width:749px;height:1200px;overflow:hidden}
body{font-family:'Montserrat',sans-serif;color:var(--ink);background:var(--white);position:relative}
.abs{position:absolute}
.topline{left:0;top:0;width:749px;height:2px;background:var(--teal)}
/* header */
.logo{left:96px;top:18px;display:flex;align-items:center;gap:6px}
.logo-dot{width:26px;height:26px;border-radius:50%;background:var(--teal)}
.logo-name{font-weight:800;font-size:17px;color:var(--navy);line-height:1}
.lang{left:631px;top:10px;font-size:7px;color:var(--teal);font-weight:600}
.nav{top:30px;font-size:6.4px;font-weight:700;color:#8a97a3;letter-spacing:.2px}
.pill{top:26px;height:17px;border-radius:9px;font-size:6.4px;font-weight:700;color:#fff;display:flex;align-items:center;justify-content:center}
.pill.login{left:541px;width:42px;background:var(--teal)}
.pill.open{left:595px;width:69px;background:var(--orange)}
/* hero */
.hero{left:85px;top:64px;width:579px;height:246px;background:linear-gradient(100deg,#15243a 0%,#2a4560 45%,#4aa6a6 62%,#5db4b0 100%)}
.hero-robot{left:352px;top:76px;width:88px;height:196px;border-radius:44px 44px 30px 30px;background:linear-gradient(180deg,#c9d1da,#8c99a8)}
.welcome{left:114px;top:169px;color:#fff;font-size:13.5px;font-weight:500}
.winning{left:114px;top:184px;color:#fff;font-size:28.5px;font-weight:800;letter-spacing:-.3px}
.gs-title{left:467px;top:88px;font-size:16px;font-weight:800;color:var(--navy)}
.field{left:467px;width:171px;height:21px;background:#fff;border:1px solid #d9e2e6;border-radius:2px;font-size:5.6px;color:#9aa6b0;padding-left:8px;display:flex;align-items:center}
.submit{left:467px;top:265px;width:107px;height:20px;border-radius:10px;background:var(--navy);color:var(--orange);font-size:6.6px;font-weight:700;display:flex;align-items:center;justify-content:center}
/* intro */
.intro{left:0;top:310px;width:749px;height:116px;background:var(--pale)}
.intro h2{position:absolute;top:23px;width:100%;text-align:center;font-size:14.5px;font-weight:700;color:#6d8a96}
.intro p{position:absolute;top:45px;left:170px;width:409px;text-align:center;font-size:10.2px;line-height:14.3px;color:#3d4a56}
.perks{left:0;top:426px;width:749px;height:80px;background:#f5fafa}
.perk{top:454px;display:flex;align-items:center;gap:10px;font-size:10.4px;font-weight:700;color:#3d4a56}
.perk svg{width:25px;height:25px}
/* why */
.why{left:0;top:506px;width:749px;height:307px;background:linear-gradient(135deg,#1d2836,#2a3745 60%,#3a4858)}
.why-robot{left:353px;top:482px;width:40px;height:82px;border-radius:20px;background:linear-gradient(180deg,#c9d1da,#8c99a8)}
.why-title{left:0;top:573px;width:749px;text-align:center;font-size:13.6px;font-weight:800;color:var(--teal)}
.icon-ring{width:42px;height:42px;border-radius:50%;border:2px solid var(--teal);display:flex;align-items:center;justify-content:center;top:604px}
.col{top:657px;width:210px;text-align:center;color:#fff}
.col h3{font-size:10.2px;font-weight:700;margin-bottom:6px}
.col p{font-size:7.6px;line-height:13.1px;font-weight:500}
.more{left:322px;top:756px;width:105px;height:19px;border-radius:10px;background:var(--teal);color:#fff;font-size:6.5px;font-weight:700;display:flex;align-items:center;justify-content:center}
/* feature */
.feat-title{left:48px;top:862px;font-size:14.5px;font-weight:800;color:var(--teal)}
.feat-text{left:48px;top:887px;width:184px;font-size:7.8px;line-height:13px;color:#3d4a56}
.bullets{left:48px;top:949px;list-style:none;font-size:7.8px;color:#3d4a56}
.bullets li{height:17px;padding-left:8px;position:relative}
.bullets li::before{content:"";position:absolute;left:0;top:4px;width:3px;height:3px;border-radius:50%;background:var(--teal)}
.cta{left:48px;top:1030px;width:106px;height:19px;border-radius:10px;background:var(--teal);color:#fff;font-size:6.5px;font-weight:700;display:flex;align-items:center;justify-content:center}
.feat-robot{left:252px;top:860px;width:90px;height:168px;border-radius:40px 40px 30px 30px;background:linear-gradient(180deg,#c9d1da,#8c99a8)}
/* dashboard */
.dash{left:344px;top:846px;width:357px;height:230px;border:1px solid #9db0c0;background:#fff}
.dash-in{left:350px;top:851px;width:346px;height:220px;border:1px solid #d5dde3}
.dash-title{position:absolute;left:6px;top:5px;font-size:9.5px;font-weight:600;color:var(--navy);line-height:1}
.t{position:absolute;font-size:3.8px;color:#4a5560;white-space:nowrap}
.tab{position:absolute;top:20px;height:11px;font-size:3.8px;display:flex;align-items:center;justify-content:center}
.sw{position:absolute;width:13px;height:6px;background:#3d8fd6;border-radius:1px}
.box{position:absolute;width:17px;height:6px;border:1px solid #c8d0d6;background:#fff}
.chk{position:absolute;width:5px;height:5px;border:1px solid #3d8fd6}
.rule{position:absolute;height:1px;background:#c8d0d6}
/* chat: sits below the dashboard, right of the footer text */
.chat{left:612px;top:1082px;width:134px;height:118px;background:var(--chat)}
.chat-head{left:612px;top:1082px;width:134px;height:14px;background:var(--navy);color:#fff;font-size:5.6px;font-weight:700;display:flex;align-items:center;padding-left:32px}
.chat-text{font-size:5.4px;color:#fff;font-weight:600;line-height:7.5px}
.chat-btn{left:620px;top:1118px;width:118px;height:12px;background:#b4bfcf;color:#fff;font-size:5.6px;display:flex;align-items:center;justify-content:center;font-weight:600}
.chat-input{left:620px;top:1170px;width:118px;height:16px;background:#c2ccd8;color:#6c7a8c;font-size:5.6px;padding:5px 6px;line-height:1}
/* footer */
.footer{left:0;top:1110px;width:749px;height:68px;background:var(--navy)}
.legal{left:88px;width:512px;text-align:center;font-size:3.9px;line-height:7.8px;color:#b8c2cc}
.bottom{left:0;top:1178px;width:749px;height:22px;background:var(--teal)}
.bnav{top:1187px;font-size:4.6px;font-weight:700;color:#2d6e6b}
</style>
</head>
<body>
<div class="abs topline"></div>

<header>
  <div class="abs logo"><span class="logo-dot"></span><span class="logo-name">Vextra Pilot</span></div>
  <div class="abs lang">English ▾</div>
  <span class="abs nav" style="left:294px">HOME</span>
  <span class="abs nav" style="left:330px">FAQs</span>
  <span class="abs nav" style="left:362px">GUIDES</span>
  <span class="abs nav" style="left:402px">CONTACT</span>
  <span class="abs nav" style="left:450px">AFFILIATE PROGRAMME</span>
  <span class="abs pill login">LOGIN</span>
  <span class="abs pill open">OPEN ACCOUNT</span>
</header>

<section>
  <div class="abs hero" role="img" aria-label="Trading screen photo with asset prices, fading into teal"></div>
  <div class="abs hero-robot" role="img" aria-label="Flying robot mascot illustration"></div>
  <div class="abs welcome">WELCOME TO VEXTRA PILOT</div>
  <div class="abs winning">Bright Paths</div>
  <div class="abs gs-title">GET STARTED</div>
  <div class="abs field" style="top:114px">FIRST NAME</div>
  <div class="abs field" style="top:143px">LAST NAME</div>
  <div class="abs field" style="top:173px">VAILID EMAIL ADDRESS</div>
  <div class="abs field" style="top:202px">CHOOSE A PASSWORD</div>
  <div class="abs field" style="top:232px;width:47px">+357</div>
  <div class="abs field" style="top:232px;left:518px;width:120px">PHONE NUMBER</div>
  <div class="abs submit">OPEN YOUR ACCOUNT</div>
</section>

<section class="abs intro">
  <h2>The Best Vextra Pilot</h2>
  <p>Vextra Pilot is a premium trading software that finds all the best opportunities from the market for you. Trade with the best brokers on the market, and benefit from this extraordinary trading experience.</p>
</section>

<section>
  <div class="abs perks"></div>
  <div class="abs perk" style="left:38px"><svg viewBox="0 0 25 25"><circle cx="12.5" cy="12.5" r="11" fill="none" stroke="var(--orange)" stroke-width="1.6"/><path d="M7.5 12.5l3.5 3.5 6.5-7" fill="none" stroke="var(--orange)" stroke-width="1.8" stroke-linecap="round"/></svg>Free Binary Trading Software</div>
  <div class="abs perk" style="left:287px"><svg viewBox="0 0 25 25"><circle cx="12.5" cy="12.5" r="11" fill="none" stroke="var(--orange)" stroke-width="1.6"/><path d="M7.5 12.5l3.5 3.5 6.5-7" fill="none" stroke="var(--orange)" stroke-width="1.8" stroke-linecap="round"/></svg>No downloads required</div>
  <div class="abs perk" style="left:511px"><svg viewBox="0 0 25 25"><circle cx="12.5" cy="12.5" r="11" fill="none" stroke="var(--orange)" stroke-width="1.6"/><path d="M7.5 12.5l3.5 3.5 6.5-7" fill="none" stroke="var(--orange)" stroke-width="1.8" stroke-linecap="round"/></svg>Multiple brokers available</div>
</section>

<section>
  <div class="abs why" role="img" aria-label="Dark photo of a trading price chart"></div>
  <div class="abs why-robot" role="img" aria-label="Small robot mascot illustration"></div>
  <div class="abs why-title">WHY CHOOSE VEXTRA PILOT? ...</div>
  <div class="abs icon-ring" style="left:116px"><svg width="16" height="18" viewBox="0 0 16 18"><path d="M4 8V5a4 4 0 0 1 8 0v3" fill="none" stroke="var(--teal)" stroke-width="2"/><rect x="2" y="8" width="12" height="9" rx="1" fill="var(--teal)"/></svg></div>
  <div class="abs icon-ring" style="left:353px"><svg width="20" height="18" viewBox="0 0 20 18"><path d="M10 2v9M6 7l4 4 4-4M2 11v5h16v-5" fill="none" stroke="var(--teal)" stroke-width="1.6"/></svg></div>
  <div class="abs icon-ring" style="left:583px"><svg width="20" height="18" viewBox="0 0 20 18"><rect x="2" y="8" width="4" height="9" fill="var(--teal)"/><path d="M7 9l4-7c2 0 2 2 1.5 5H18v3l-2 7H7z" fill="var(--teal)"/></svg></div>
  <div class="abs col" style="left:32px"><h3>Safe &amp; Secure - Automatic stop loss</h3><p>Lorem ipsum dolor sit amet, consectetur adipiscing elit, sed do eiusmod tempor incididunt ut labore et dolore magna aliqua. Ut enim ad minim veniam, quis nostrud exercitation ullamco laboris nisi ut aliquip ex ea commodo.</p></div>
  <div class="abs col" style="left:269px"><h3>No Downloads - No Charges</h3><p>Ut enim ad minim veniam, quis nostrud exercitation ullamco laboris nisi ut aliquip ex ea commodo consequat. Duis aute irure dolor in reprehenderit in voluptate velit esse cillum dolore eu fugiat nulla pariatur.</p></div>
  <div class="abs col" style="left:501px"><h3>Trusted Vextra Pilot</h3><p>Duis aute irure dolor in reprehenderit in voluptate velit esse cillum dolore eu fugiat nulla pariatur. Excepteur sint occaecat cupidatat non proident, sunt in culpa qui officia deserunt mollit anim id est laborum.</p></div>
  <div class="abs more">FIND OUT MORE</div>
</section>

<section>
  <div class="abs feat-title">HEADER IN HERE</div>
  <p class="abs feat-text">Lorem ipsum dolor sit amet adipiscing elit, sed do eiusmod tempor incididunt labore et dolore magna aliqua. Ut enim ad minim veniam, quis nostrud exercitation:</p>
  <ul class="abs bullets">
    <li>Lorem ipsum dolor sit amet adipiscing</li>
    <li>Sed do eiusmod tempor incididunt labore</li>
    <li>Ut enim ad minim veniam quis nostrud</li>
    <li>Ullamco laboris nisi aliquip consequat</li>
  </ul>
  <div class="abs cta">GET STARTED</div>
  <div class="abs feat-robot" role="img" aria-label="Waving robot mascot illustration"></div>

  <div class="abs dash"></div>
  <div class="abs dash-in">
    <div class="dash-title">Dashboard</div>
    <div class="tab" style="left:6px;width:90px;background:#dfe6ec;color:#4a5560">Robot Settings</div>
    <div class="tab" style="left:96px;width:107px;background:var(--navy);color:#fff">Trading Room</div>
    <div class="tab" style="left:203px;width:107px;background:var(--navy);color:#fff">History</div>
    <span class="t" style="left:10px;top:36px">Brokers</span><span class="t" style="left:74px;top:36px">Balance</span><span class="t" style="left:128px;top:36px">Open Trades</span><span class="t" style="left:170px;top:36px">Profit</span><span class="t" style="left:213px;top:36px">Active Trading</span><span class="t" style="left:298px;top:36px">Deposit</span><span class="t" style="left:325px;top:36px">More settings</span>
    <div class="rule" style="left:6px;top:44px;width:334px"></div>
    <span class="t" style="left:6px;top:52px;background:#2a2320;color:#f0a500;padding:2px 3px;font-weight:700">CRESTLINE</span>
    <span class="t" style="left:70px;top:54px">€16,619.75</span><span class="t" style="left:144px;top:54px">€5</span><span class="t" style="left:188px;top:54px">€14,929.25</span>
    <div class="sw" style="left:242px;top:53px"></div>
    <span class="t" style="left:286px;top:52px;background:var(--orange);color:#fff;padding:1px 4px">Deposit</span>
    <span style="position:absolute;left:322px;top:52px;width:8px;height:8px;border-radius:50%;background:#e06a3a"></span>
    <div class="rule" style="left:6px;top:66px;width:334px;background:#5e6a76;height:2px"></div>
    <span class="t" style="left:30px;top:72px;font-size:4.6px">Trade Options</span><span class="t" style="left:240px;top:72px;font-size:4.6px">Trade Options</span>
    <span class="t" style="left:8px;top:85px">Daily Stop Loss</span><div class="box" style="left:70px;top:84px"></div><span class="t" style="left:73px;top:85px">500</span>
    <span class="t" style="left:8px;top:101px">Max Daily Trades</span><div class="box" style="left:70px;top:100px"></div><span class="t" style="left:73px;top:101px">80</span>
    <span class="t" style="left:103px;top:85px">USDJPY</span><div class="sw" style="left:137px;top:84px"></div>
    <span class="t" style="left:103px;top:100px">EURGBP</span><div class="sw" style="left:137px;top:99px"></div>
    <span class="t" style="left:103px;top:115px">USDCHF</span><div class="sw" style="left:137px;top:114px"></div>
    <span class="t" style="left:185px;top:85px">AUDUSD</span><div class="sw" style="left:219px;top:84px"></div>
    <span class="t" style="left:185px;top:100px">EURUSD</span><div class="sw" style="left:219px;top:99px"></div>
    <span class="t" style="left:185px;top:115px">GBPCHF</span><div class="sw" style="left:219px;top:114px"></div>
    <span class="t" style="left:268px;top:85px">USDCAD</span><div class="sw" style="left:302px;top:84px"></div>
    <span class="t" style="left:268px;top:100px">GBPUSD</span><div class="sw" style="left:302px;top:99px"></div>
    <span class="t" style="left:268px;top:115px">GBPJPY</span><div class="sw" style="left:302px;top:114px"></div>
    <span class="t" style="left:228px;top:126px;font-size:4.6px">Market Types</span>
    <span class="t" style="left:104px;top:139px">Currencies Amount</span><div class="box" style="left:180px;top:138px"></div><span class="t" style="left:184px;top:139px">5</span>
    <span class="t" style="left:214px;top:139px">Commodities Amount</span><div class="box" style="left:288px;top:138px"></div><span class="t" style="left:292px;top:139px">25</span>
    <span class="t" style="left:104px;top:154px">Pairs Amount</span><div class="box" style="left:180px;top:153px"></div><span class="t" style="left:184px;top:154px">25</span>
    <span class="t" style="left:214px;top:154px">Indices Amount</span><div class="box" style="left:288px;top:153px"></div><span class="t" style="left:292px;top:154px">25</span>
    <span class="t" style="left:190px;top:166px;font-size:4.6px">VIP Features</span>
    <span class="t" style="left:190px;top:172px;font-size:3.3px">Signal providers</span>
    <div style="position:absolute;left:6px;top:177px;width:100px;height:32px;border:1px solid #d5dde3"></div>
    <span class="t" style="left:46px;top:180px">Risk Level</span>
    <div style="position:absolute;left:14px;top:188px;width:84px;height:7px;background:linear-gradient(90deg,#6cc04a,#d8d23a 35%,#f0a500 60%,#e03a2a)"></div>
    <span class="t" style="left:44px;top:199px">Level 1 of 4</span>
    <div style="position:absolute;left:114px;top:177px;width:182px;height:32px;border:1px solid #d5dde3"></div>
    <div class="chk" style="left:120px;top:190px"></div><span class="t" style="left:128px;top:190px">Strategy 1</span>
    <div class="chk" style="left:162px;top:190px"></div><span class="t" style="left:170px;top:190px">Strategy 2</span>
    <div class="chk" style="left:204px;top:190px"></div><span class="t" style="left:212px;top:190px">Strategy 3</span>
    <div class="chk" style="left:246px;top:190px"></div><span class="t" style="left:254px;top:190px">Strategy 4</span>
  </div>
</section>

<footer>
  <div class="abs footer"></div>
  <p class="abs legal" style="top:1126px">Information on quellmarktrader.com should not be seen as a recommendation to trade binary options. quellmarktrader.com is a free software that enables you to receive free binary signals from 3rd parties. quellmarktrader.com is not authorized to provide advice on investing and related matters. Information on the website is not, nor should it be seen as investment advice. Clients without sufficient knowledge should seek individual advice from an authorized source. Trading entails significant risks and there is a chance that clients lose their investments. Past performance is not a guarantee of future returns.</p>
  <p class="abs legal" style="top:1158px">Our software is independent of binary brokers featured herein. Before trading with any of the brokers, clients should make sure they understand the risks involved. We recommend choosing an EU regulated broker for citizens residing in Europe.</p>
  <div class="abs bottom"></div>
  <span class="abs bnav" style="left:33px">HOME</span>
  <span class="abs bnav" style="left:61px">FAQs</span>
  <span class="abs bnav" style="left:86px">GUIDES</span>
  <span class="abs bnav" style="left:118px">CONTACT</span>
  <span class="abs bnav" style="left:155px">LOGIN</span>
  <span class="abs bnav" style="left:183px">OPEN ACCOUNT</span>
  <span class="abs bnav" style="left:237px">AFFILIATE PROGRAMME</span>
  <span class="abs bnav" style="left:580px;color:#fff">© 2016</span>
</footer>

<aside>
  <div class="abs chat"></div>
  <div class="abs chat-head">HOW CAN WE HELP?<span style="position:absolute;right:6px">↗ _</span></div>
  <div class="abs chat-text" style="left:620px;top:1100px">SUPPORT AGENT<br>Live Support</div>
  <div class="abs chat-btn">CHAT STARTED</div>
  <div class="abs chat-text" style="left:620px;top:1134px;width:122px">CUSTOMER SERVICE<br>Hi there! You can chat with us right here. Don't forget to leave your email. Thank you.</div>
  <div class="abs chat-input">Type your message here</div>
  <div class="abs chat-text" style="left:620px;top:1189px">Options &nbsp;&nbsp;&nbsp; Sign In</div>
</aside>
</body>
</html>
```